Baby acupressure app for parents

We need an app for parents that teaches parents how to help them relieve their baby's imbalances (stomach ache, trouble sleeping etc.)

Please see the attached document (with info) and wireframes.

This project is urgent so please only participate if you're able to finish all screens within a few days after the contest is over.

Target Market(s)

Baby moms (20-40 years of age)

Industry/Entity Type

Baby Care

Colors
886aae
b768aa
e667a6
f68d4d
faa54b
fac994
f9ba93
f59195
fee18a

Requirements
Must have
• A high quality design that is both modern and very sleek and stylish.
Nice to have
• Simple animations to make the app "feel" like it's extreme high quality and make the user want to use it again and again
Should not have
• Sandwich menus

```html
<!DOCTYPE html>
<html lang="en">
<head>
<meta charset="utf-8">
<title>Ear pain</title>
<link href="https://fonts.googleapis.com/css2?family=Montserrat:wght@300;400;600;700&display=swap" rel="stylesheet">
<style>
  :root {
    --bg: #f8e6f0;
    --top-band: #cc6aa0;
    --purple: #8860b8;
    --purple-text: #9b79c0;
    --purple-strong: #8a5cb4;
    --magenta: #b05aaa;
    --white: #ffffff;
    --photo-a: #c9c2bc;
    --photo-b: #e9d6cc;
    --photo-c: #ece8e4;
    --photo-d: #d8c4b8;
  }
  * { box-sizing: border-box; margin: 0; padding: 0; }
  html, body { width: 1200px; height: 2644px; overflow: hidden; }
  body {
    position: relative;
    background: var(--bg);
    font-family: "Montserrat", sans-serif;
    font-weight: 300;
    color: var(--purple-text);
  }
  .top-band { position: absolute; left: 0; top: 0; width: 1200px; height: 238px; background: var(--top-band); }

  .topic-card {
    position: absolute; left: 38px; top: 75px; width: 1125px; height: 994px;
    border-radius: 38px; overflow: hidden; background: var(--purple);
    box-shadow: 0 14px 28px rgba(90, 50, 110, 0.28);
  }
  .topic-header { position: relative; height: 163px; }
  .back-link {
    position: absolute; left: 22px; top: 50%; transform: translateY(-50%);
    display: flex; align-items: center; gap: 8px;
    color: var(--white); font-size: 45px; font-weight: 300;
  }
  .back-link svg { width: 34px; height: 52px; }
  .topic-title {
    position: absolute; left: 0; right: 0; top: 50%; transform: translateY(-50%);
    text-align: center; color: var(--white); font-size: 82px; font-weight: 600;
  }
  .video-area {
    position: relative; height: 634px;
    background: linear-gradient(120deg, var(--photo-a) 0%, var(--photo-b) 55%, #b9b4b8 100%);
  }
  .play-button {
    position: absolute; left: 472px; top: 253px; width: 180px; height: 180px;
    border-radius: 50%; background: var(--white);
    display: flex; align-items: center; justify-content: center;
  }
  .play-button svg { width: 50px; height: 50px; margin-left: 8px; }
  .topic-summary { position: relative; height: 197px; }
  .summary-toggle { position: absolute; left: 42px; top: 60px; width: 66px; height: 66px; }
  .summary-text {
    position: absolute; left: 155px; top: 20px; width: 910px;
    color: var(--white); font-size: 34px; line-height: 49px; font-weight: 300;
  }

  .intro-text {
    position: absolute; left: 43px; top: 1140px; width: 1120px;
    font-size: 45px; line-height: 58px;
  }
  .treatment-photo {
    position: absolute; left: 38px; top: 1312px; width: 1125px; height: 610px;
    background: linear-gradient(90deg, var(--photo-c) 0%, var(--photo-b) 45%, var(--photo-d) 100%);
  }
  .bonus-text {
    position: absolute; left: 43px; top: 1969px; width: 1120px;
    font-size: 45px; line-height: 58px;
  }
  .bonus-text strong { font-weight: 700; color: var(--purple-strong); }
  .more-details {
    position: absolute; left: 43px; top: 2119px;
    font-size: 41px; font-weight: 700; letter-spacing: 1px; color: var(--purple-strong);
  }
  .start-button {
    position: absolute; left: 319px; top: 2235px; width: 562px; height: 131px;
    border-radius: 66px; background: var(--magenta);
    display: flex; align-items: center; justify-content: center;
    color: var(--white); font-size: 45px; font-weight: 400; letter-spacing: 15px; padding-left: 15px;
  }

  .tab-bar { position: absolute; left: 0; top: 2460px; width: 1200px; height: 184px; background: var(--white); }
  .tab-active-disc {
    position: absolute; left: 326px; top: 2456px; width: 262px; height: 262px;
    border-radius: 50%; background: var(--magenta);
  }
  .tab {
    position: absolute; top: 2490px; width: 220px; margin-left: -110px;
    display: flex; flex-direction: column; align-items: center;
    color: var(--magenta); font-size: 30px; font-weight: 400;
  }
  .tab svg { width: 84px; height: 84px; margin-bottom: 14px; }
  .tab.is-active { color: var(--white); }
</style>
</head>
<body>
  <div class="top-band"></div>

  <section class="topic-card">
    <header class="topic-header">
      <div class="back-link">
        <svg viewBox="0 0 34 52"><path d="M26 6 L8 26 L26 46" fill="none" stroke="#fff" stroke-width="4" stroke-linecap="round" stroke-linejoin="round"/></svg>
        <span>Back</span>
      </div>
      <h1 class="topic-title">Ear pain</h1>
    </header>
    <div class="video-area" role="img" aria-label="Video still of a crying baby holding a hand to its ear">
      <div class="play-button">
        <svg viewBox="0 0 50 50"><path d="M6 3 L46 25 L6 47 Z" fill="#9a5cb0"/></svg>
      </div>
    </div>
    <div class="topic-summary">
      <svg class="summary-toggle" viewBox="0 0 66 66"><circle cx="33" cy="33" r="31" fill="none" stroke="#7a52a8" stroke-width="2.5"/><path d="M33 50 V16 M20 29 L33 16 L46 29" fill="none" stroke="#7a52a8" stroke-width="2.5" stroke-linecap="round" stroke-linejoin="round"/></svg>
      <p class="summary-text">This is some text about the ear pain. What could be the reasons for it, is it normal/abnormal, symptoms etc.</p>
    </div>
  </section>

  <p class="intro-text">There are multiple ways to trigger some positive effects and you can try out multiple treatments...</p>

  <div class="treatment-photo" role="img" aria-label="Photo of a doctor checking a baby's ear with an otoscope"></div>

  <p class="bonus-text">Also, check out the bonus info from <strong>name</strong> who also offers some great advice on this topic!</p>
  <div class="more-details">MORE DETAILS...</div>

  <div class="start-button">START NOW</div>

  <nav>
    <div class="tab-bar"></div>
    <div class="tab-active-disc"></div>
    <div class="tab" style="left:178px">
      <svg viewBox="0 0 84 84"><path d="M10 40 L42 10 L74 40 M18 33 V74 H66 V33 M34 74 V50 H50 V74" fill="none" stroke="#b05aaa" stroke-width="3" stroke-linejoin="round" stroke-linecap="round"/></svg>
      <span>Home</span>
    </div>
    <div class="tab is-active" style="left:457px">
      <svg viewBox="0 0 84 84"><path d="M44 8 H74 V38 L38 74 L8 44 Z" fill="none" stroke="#fff" stroke-width="3" stroke-linejoin="round"/><circle cx="60" cy="22" r="5" fill="none" stroke="#fff" stroke-width="3"/></svg>
      <span>Imbalances</span>
    </div>
    <div class="tab" style="left:741px">
      <svg viewBox="0 0 84 84"><path d="M56 20 H10 V74 H64 V56" fill="none" stroke="#b05aaa" stroke-width="3" stroke-linejoin="round"/><path d="M22 58 C24 38 38 30 58 30 V18 L78 36 L58 54 V42 C42 42 30 46 22 58 Z" fill="none" stroke="#b05aaa" stroke-width="3" stroke-linejoin="round"/></svg>
      <span>Share</span>
    </div>
    <div class="tab" style="left:1022px">
      <svg viewBox="0 0 84 84"><circle cx="42" cy="42" r="36" fill="none" stroke="#b05aaa" stroke-width="3"/><circle cx="42" cy="26" r="3" fill="#b05aaa"/><path d="M42 36 V60" stroke="#b05aaa" stroke-width="3" stroke-linecap="round"/></svg>
      <span>About</span>
    </div>
  </nav>
</body>
</html>
```